Communication Coach needs a business card

https://imgvaultcdn.example/design_img/3817205/61824/61824_27395018_3817205_8c2e7d1b_thumbnail.png

I like this a lot

I want it to include the following

Delia Fenwick
M.A.CCC-SLP
628-417-2093
delia.fenwick@quillpost.example
Communication Trainer and Executive Function Coaching
Be Confident-Be Authentic- Be Memorable

on back of card
Public Speaking
Executive Function Coaching
Interview Skills
Corporate Workshops
Self Regulation/Confidence Building

Target Market(s)

adults, parents

Contact Information for Business Card

See above description. i included picture of what i like

Requirements
Must have
• two sides, multi colors ,double sided
Nice to have
• I could have a tag line on front such as Be confident-Be memorable -Be authentic
Should not have
• not too busy or creative as needs to work for corporate setting

```html
<!DOCTYPE html>
<html lang="en">
<head>
<meta charset="utf-8">
<title>Delia Fenwick – Business Card</title>
<link rel="stylesheet" href="https://fonts.googleapis.com/css2?family=Lobster&family=Poppins:wght@300;400;500;600&family=Cinzel:wght@400&display=swap">
<style>
  :root {
    --backdrop: #cbcbcb;
    --ink: #1f1f1f;
    --paper-text: #ffffff;
    --pink: #e8058f;
    --crimson: #c31f36;
    --aqua: #38fbe8;
    --blue: #2557d6;
    --orange: #fa5826;
    --gold: #f2d640;
    --lemon: #fbf06a;
  }
  * { box-sizing: border-box; margin: 0; padding: 0; }
  html, body {
    width: 1200px; height: 900px; overflow: hidden;
    background: var(--backdrop);
  }
  .sheet {
    position: relative; width: 1200px; height: 900px;
    display: flex; flex-direction: column; align-items: center; justify-content: center; gap: 44px;
  }
  .card {
    position: relative; width: 700px; height: 400px;
    border-radius: 30px; overflow: hidden;
    box-shadow: 0 6px 14px rgba(0,0,0,0.25);
  }

  /* Back side: service stripes */
  .card--services { display: flex; }
  .stripe {
    height: 100%; display: flex; align-items: center; justify-content: center;
    color: var(--paper-text);
    font-family: "Poppins", sans-serif; font-weight: 500;
    font-size: 17px; letter-spacing: 0.5px; text-transform: uppercase;
  }
  .stripe--edge { width: 8%; background: var(--gold); }
  .stripe--service { width: 16.8%; }
  .stripe__label {
    writing-mode: vertical-rl; transform: rotate(180deg);
    text-align: center; line-height: 1.25;
  }
  .stripe--pink { background: var(--pink); }
  .stripe--crimson { background: var(--crimson); }
  .stripe--aqua { background: var(--aqua); }
  .stripe--blue { background: var(--blue); }
  .stripe--orange { background: var(--orange); }

  /* Front side: contact details */
  .card--contact { background: var(--ink); color: var(--paper-text); }
  .edge-band {
    position: absolute; left: 0; width: 100%; height: 34px; display: flex;
  }
  .edge-band--top { top: 0; }
  .edge-band--bottom { bottom: 0; }
  .edge-band span { flex: 1; }
  .band-pink { background: var(--pink); }
  .band-lemon { background: var(--lemon); }
  .band-crimson { background: var(--crimson); }
  .band-aqua { background: var(--aqua); }
  .band-blue { background: var(--blue); }
  .band-orange { background: var(--orange); }

  .contact {
    position: absolute; top: 34px; bottom: 34px; left: 0; right: 0;
    display: flex; flex-direction: column; align-items: center; justify-content: center;
    text-align: center;
  }
  .contact__name {
    font-family: "Lobster", cursive; font-weight: 400;
    font-size: 62px; line-height: 1; letter-spacing: 1px;
  }
  .contact__credentials {
    font-family: "Poppins", sans-serif; font-weight: 400;
    font-size: 15px; letter-spacing: 1px;
    align-self: center; margin: 2px 0 10px 150px;
  }
  .contact__rule { width: 540px; height: 1.5px; background: var(--paper-text); }
  .contact__line {
    font-family: "Poppins", sans-serif; font-weight: 300;
    font-size: 24px; padding: 6px 0 6px;
  }
  .contact__title {
    font-family: "Cinzel", serif; font-weight: 400;
    font-size: 23px; line-height: 1.15; margin-top: 12px; letter-spacing: 0.5px;
  }
  .contact__tagline {
    font-family: "Poppins", sans-serif; font-weight: 500;
    font-size: 16px; margin-top: 12px; letter-spacing: 0.3px;
  }
</style>
</head>
<body>
<main class="sheet">

  <section class="card card--services" aria-label="Card back: services">
    <div class="stripe stripe--edge"></div>
    <div class="stripe stripe--service stripe--pink"><span class="stripe__label">Public Speaking</span></div>
    <div class="stripe stripe--service stripe--crimson"><span class="stripe__label">Executive Function<br>Coaching</span></div>
    <div class="stripe stripe--service stripe--aqua"><span class="stripe__label">Interview Skills</span></div>
    <div class="stripe stripe--service stripe--blue"><span class="stripe__label">Corporate Workshops</span></div>
    <div class="stripe stripe--service stripe--orange"><span class="stripe__label">Self Regulation/<br>Confidence Building</span></div>
    <div class="stripe stripe--edge"></div>
  </section>

  <section class="card card--contact" aria-label="Card front: contact">
    <div class="edge-band edge-band--top">
      <span class="band-pink"></span><span class="band-lemon"></span><span class="band-crimson"></span>
      <span class="band-aqua"></span><span class="band-blue"></span><span class="band-orange"></span>
    </div>
    <div class="contact">
      <h1 class="contact__name">Delia Fenwick</h1>
      <p class="contact__credentials">M.A.CCC-SLP</p>
      <div class="contact__rule"></div>
      <p class="contact__line">628-417-2093 | delia.fenwick@quillpost.example</p>
      <div class="contact__rule"></div>
      <p class="contact__title">COMMUNICATION TRAINER AND EXECUTIVE<br>FUNCTION COACHING</p>
      <p class="contact__tagline">Be Confident-Be Authentic- Be Memorable</p>
    </div>
    <div class="edge-band edge-band--bottom">
      <span class="band-pink"></span><span class="band-lemon"></span><span class="band-crimson"></span>
      <span class="band-aqua"></span><span class="band-blue"></span><span class="band-orange"></span>
    </div>
  </section>

</main>
</body>
</html>
```